Professional Services - letterhead / business cards

The company (veltaro holdings) will provide services to Investment Funds and large investors in Spain. I have recently chosen a logo that I am attaching.

I would like a simple stationary design that i could use as letter head, business cards and "with compliments" cards.

I am not quite sure which color I will mostly use for the logo, in the email signature I will probably lean towards the white background and grey letters. I am attaching my favourite options.

Target Market(s)

Large Multinationals, Investment funds and Law firms

Industry/Entity Type

Business

Requirements
Must have
• my details are:
Luis R. Andrade
Veltaro Holdings S.L.
Casa de Valdehondo
Calle del Olmo Tardío 42
28017 Madrid
T: +34 (91) 807-3356
M: +34 (655) 718-904
e-mail: landrade@veltaroholdings.example

```html
<!DOCTYPE html>
<html lang="en">
<head>
<meta charset="utf-8">
<title>Veltaro Holdings – Business Cards</title>
<link rel="stylesheet" href="https://fonts.googleapis.com/css2?family=Questrial&display=swap">
<style>
  :root {
    --navy-deep: #232a66;
    --navy: #2f3580;
    --navy-light: #4a4f95;
    --paper: #f1f1f1;
    --paper-shade: #e4e4e4;
    --rule-grey: #8a8a8a;
    --icon-grey: #5a5a5a;
    --ink-navy: #2b2f73;
    --white: #ffffff;
    --backdrop: #e9e9e9;
  }
  * { margin: 0; padding: 0; box-sizing: border-box; }
  html, body { width: 1200px; height: 900px; overflow: hidden; }
  body {
    background: radial-gradient(ellipse at 50% 45%, #fafafa 0%, var(--backdrop) 70%, #d6d6d6 100%);
    font-family: "Questrial", "Century Gothic", sans-serif;
    position: relative;
  }
  .card {
    position: absolute;
    width: 600px;
    height: 343px;
    left: 300px;
    border-radius: 2px;
    overflow: hidden;
    box-shadow: 0 10px 24px rgba(0,0,0,0.18), 0 2px 5px rgba(0,0,0,0.12);
  }
  .card--front {
    top: 70px;
    background: radial-gradient(ellipse at 50% 75%, var(--navy-light) 0%, var(--navy) 55%, var(--navy-deep) 100%);
    display: flex;
    align-items: center;
    justify-content: center;
  }
  .card--back { top: 487px; background: var(--navy); }

  .wordmark {
    color: var(--white);
    font-size: 34px;
    letter-spacing: 0.5px;
    white-space: nowrap;
  }
  .card--back .wordmark {
    color: var(--ink-navy);
    font-size: 30px;
  }

  .back__header {
    position: absolute; left: 0; top: 0; width: 100%; height: 150px;
    background: linear-gradient(180deg, var(--paper) 0%, var(--paper-shade) 100%);
    padding: 88px 0 0 52px;
  }
  .back__rule {
    position: absolute; left: 0; top: 150px; width: 100%; height: 7px;
    background: var(--rule-grey);
    border-bottom: 2px solid #bdbdbd;
  }
  .back__tab { position: absolute; left: 468px; top: 157px; }
  .back__body {
    position: absolute; left: 0; top: 159px; width: 100%; height: 184px;
    background: radial-gradient(ellipse at 40% 60%, var(--navy-light) 0%, var(--navy) 50%, var(--navy-deep) 100%);
    color: var(--white);
  }
  .back__divider {
    position: absolute; left: 392px; top: 22px; width: 1px; height: 138px;
    background: rgba(255,255,255,0.75);
  }
  .holder-name {
    position: absolute; left: 414px; top: 24px;
    font-size: 21px; letter-spacing: 0.3px;
  }
  .contact {
    position: absolute; left: 30px; top: 18px;
    list-style: none; font-size: 13px; line-height: 16px;
  }
  .contact__item { display: flex; align-items: flex-start; gap: 10px; margin-bottom: 6px; }
  .contact__icon { flex: none; width: 16px; height: 16px; margin-top: 1px; }
  .contact__lines span { display: block; }
</style>
</head>
<body>

  <section class="card card--front" aria-label="Business card front">
    <p class="wordmark">veltaro holdings</p>
  </section>

  <section class="card card--back" aria-label="Business card back">
    <header class="back__header">
      <p class="wordmark">veltaro holdings</p>
    </header>
    <div class="back__rule"></div>
    <div class="back__body">
      <ul class="contact">
        <li class="contact__item">
          <svg class="contact__icon" viewBox="0 0 16 16" aria-hidden="true">
            <circle cx="8" cy="8" r="8" fill="var(--icon-grey)"/>
            <path d="M8 3.5a2.8 2.8 0 0 0-2.8 2.8c0 2 2.8 5.2 2.8 5.2s2.8-3.2 2.8-5.2A2.8 2.8 0 0 0 8 3.5z" fill="#fff"/>
            <circle cx="8" cy="6.3" r="1" fill="var(--icon-grey)"/>
          </svg>
          <div class="contact__lines">
            <span>Veltaro Holdings S.L.</span>
            <span>Casa de Valdehondo, Calle del Olmo Tardío 42</span>
            <span>28017 Madrid</span>
          </div>
        </li>
        <li class="contact__item">
          <svg class="contact__icon" viewBox="0 0 16 16" aria-hidden="true">
            <circle cx="8" cy="8" r="8" fill="var(--icon-grey)"/>
            <path d="M4.5 6.5c0-1.2 1.6-2 3.5-2s3.5.8 3.5 2v.6h-1.6v-.8H6.1v.8H4.5z M5.5 8h5l.8 3.5H4.7z" fill="#fff"/>
          </svg>
          <div class="contact__lines"><span>+34 (91) 807-3356</span></div>
        </li>
        <li class="contact__item">
          <svg class="contact__icon" viewBox="0 0 16 16" aria-hidden="true">
            <circle cx="8" cy="8" r="8" fill="var(--icon-grey)"/>
            <rect x="5.5" y="3.5" width="5" height="9" rx="0.8" fill="#fff"/>
            <rect x="6.3" y="4.6" width="3.4" height="5" fill="var(--icon-grey)"/>
          </svg>
          <div class="contact__lines"><span>+34 (655) 718-904</span></div>
        </li>
        <li class="contact__item">
          <svg class="contact__icon" viewBox="0 0 16 16" aria-hidden="true">
            <circle cx="8" cy="8" r="8" fill="var(--icon-grey)"/>
            <text x="8" y="11.3" text-anchor="middle" font-size="10" fill="#fff" font-family="Questrial, sans-serif">@</text>
          </svg>
          <div class="contact__lines"><span>landrade@veltaroholdings.example</span></div>
        </li>
      </ul>
      <div class="back__divider"></div>
      <p class="holder-name">Luis R. Andrade</p>
    </div>
    <svg class="back__tab" width="52" height="14" viewBox="0 0 52 14" aria-hidden="true">
      <polygon points="0,0 52,0 36,14 16,14" fill="var(--rule-grey)"/>
    </svg>
  </section>

</body>
</html>
```